Web Design Project for Velmoreq Civic

Need a website designed, coded and implemented on our server for a subdomain of our main web site velmoreq.example to promote commercial outdoor furniture products and a modular deck product. The requirements are hopefully explained in sufficient detail in the attached word document.

I understand at first the budget on the project is low but I'm looking to see the designs submitted first then once I have chosen a winner, I will increase the budget with what will be agreed on between me and the winning designer.

```html
<!DOCTYPE html>
<html lang="en">
<head>
<meta charset="utf-8">
<title>Velmoreq Civic — Street Life × Town Life</title>
<link href="https://fonts.googleapis.com/css2?family=Raleway:wght@300;400;500;600;700&display=swap" rel="stylesheet">
<style>
:root{
  --teal:#1d6f79;
  --teal-dark:#1c4b53;
  --teal-deep:#15606a;
  --ink:#3b3b3b;
  --muted:#666;
  --light:#f2f2f2;
  --white:#fff;
}
*{box-sizing:border-box;margin:0;padding:0}
html,body{width:1200px;height:4936px;overflow:hidden}
body{font-family:"Raleway",sans-serif;color:var(--ink);background:var(--white);position:relative}
section,footer{overflow:hidden}
.topbar{height:12px;background:var(--teal)}
.header{height:68px;display:flex;align-items:center;justify-content:space-between;padding:0 40px 0 160px;background:var(--white)}
.brand{display:flex;align-items:center;gap:8px;font-weight:600;font-size:17px;color:var(--teal)}
.brand i{width:12px;height:12px;background:var(--teal);display:block}
.nav{display:flex;gap:24px;font-size:12px;font-weight:500;color:#444}
.nav .active{color:var(--teal)}
.photo{position:relative;color:var(--white)}
.photo .bg{position:absolute;inset:0}
.photo .shade{position:absolute;inset:0;background:rgba(20,22,24,.45)}
.photo .inner{position:relative;height:100%;display:flex;flex-direction:column;align-items:center;justify-content:center;text-align:center}
.hero{height:720px}
.hero .bg{background:linear-gradient(120deg,#6f7478 0%,#4d5256 35%,#8a8a5a 60%,#c9b84a 75%,#5a5e60 100%)}
.hero .tag{font-size:22px;letter-spacing:5px;font-weight:400;margin-top:-100px}
.hero h1{font-size:60px;font-weight:700;letter-spacing:2px;margin:18px 0 34px;display:flex;gap:44px;align-items:center}
.hero h1 span{font-weight:300;font-size:36px}
.hero p{font-size:13px;max-width:720px;line-height:1.8}
.pillars{height:400px;background:var(--light);display:flex;gap:8px;padding:88px 168px 0}
.pillar{width:284px;height:240px;background:var(--white);padding:48px 36px 0;box-shadow:0 1px 4px rgba(0,0,0,.12);position:relative}
.pillar h3{font-size:19px;font-weight:500;color:var(--teal-dark);letter-spacing:1px}
.pillar p{font-size:10.5px;margin-top:10px;line-height:1.5;color:var(--muted);width:130px}
.pillar .pic{position:absolute;right:24px;bottom:24px;width:120px;height:90px;border-radius:3px}
.btn{display:inline-block;background:var(--teal);color:var(--white);font-size:11px;font-weight:700;letter-spacing:1px;padding:12px 22px;margin-top:26px}
.parklet{height:548px}
.parklet .bg{background:linear-gradient(100deg,#2f3234 0%,#5b5f5f 40%,#8b8f88 55%,#3c4042 100%)}
.parklet .box{width:576px;height:380px;border:3px solid rgba(255,255,255,.85);background:rgba(30,32,34,.55);display:flex;flex-direction:column;align-items:center;justify-content:center;margin-top:-40px}
.darkline h2{font-size:34px;font-weight:600;letter-spacing:1px}
.darkline ul{list-style:none;margin-top:22px;font-size:13px;line-height:1.9}
.split{display:flex;justify-content:space-between;padding:0 160px}
.split .copy{width:420px;padding-top:90px;flex-shrink:0}
.split h2{font-size:35px;font-weight:500;color:var(--teal);line-height:1.2;letter-spacing:1px}
.split ul{list-style:none;font-size:13px;line-height:2;margin-top:20px;color:var(--ink)}
.tiles{display:grid;gap:14px;padding-top:96px;align-content:start}
.tile{border:1px solid #ddd;border-radius:3px;background:var(--white);display:flex;align-items:center;justify-content:center}
.tile div{width:78%;height:62%;border-radius:3px}
.cafe{height:484px}
.cafe .tiles{grid-template-columns:220px 220px;grid-template-rows:120px 140px}
.cafe .tile.wide{grid-column:2}
.porcelain{height:428px}
.porcelain .bg{background:linear-gradient(160deg,#4a4e50,#2e6f8a 45%,#6b6f70 70%,#3b3e40)}
.porcelain h2{font-size:38px;line-height:1.25}
.porcelain ul{margin-top:14px}
.porcelain .btn{margin-top:20px}
.bench{height:480px}
.bench .tiles{grid-template-columns:200px 200px;grid-template-rows:150px 150px}
.bench .tile.wide{grid-column:1/3}
.illum{height:420px}
.illum .bg{background:linear-gradient(90deg,#2a2b2c 0%,#3a3a3a 55%,#bfbfbf 78%,#6d6d6d 100%)}
.modular{height:440px}
.modular .tiles{grid-template-columns:200px 200px;grid-template-rows:270px;padding-top:70px}
.modular .tile div{height:70%}
.solar{height:392px}
.solar .bg{background:linear-gradient(180deg,#5d6670 0%,#8a8c8a 45%,#4e5a50 100%)}
.footer{height:496px;background:var(--teal-dark);color:#e7eef0;padding:64px 160px 0;display:flex;justify-content:space-between}
.footer h4{font-size:13px;font-weight:600;letter-spacing:1px;margin-bottom:26px}
.footer .about{width:320px}
.footer .about p{font-size:10.5px;line-height:2}
.footer ul{list-style:none;font-size:10.5px;line-height:2.4;letter-spacing:.5px}
.footer ul li{text-decoration:underline}
.footer .res{width:240px;margin-left:140px}
.footer .quick{width:150px}
.social{width:26px;height:26px;background:#d9e2e4;margin-top:14px}
.bottombar{height:48px;background:var(--teal-deep);color:#dfe9eb;font-size:11px;display:flex;align-items:center;justify-content:center}
</style>
</head>
<body>
<div class="topbar"></div>
<header class="header">
  <div class="brand"><i></i>Velmoreq Civic</div>
  <nav class="nav">
    <span class="active">Home</span><span>About Us</span><span>CurbLine Kits</span><span>Products ▾</span><span>Collections ▾</span><span>Gallery</span><span>Contact Us</span>
  </nav>
</header>

<section class="photo hero">
  <div class="bg" role="img" aria-label="City sidewalk with a bright yellow bench and planters"></div>
  <div class="shade"></div>
  <div class="inner">
    <div class="tag">Bringing Space, Color &amp; Light to Urban Environments</div>
    <h1>STREET LIFE <span>×</span> TOWN LIFE</h1>
    <p>"CurbLine is a modular deck system that widens footpaths into lively public places, paired with durable commercial seating and planters built for everyday civic use."</p>
  </div>
</section>

<section class="pillars">
  <div class="pillar"><h3>SPACE</h3><p>CurbLine Kits for Parklets &amp; outdoor dining</p><div class="pic" role="img" aria-label="Black parklet deck with planters" style="background:linear-gradient(135deg,#2b2b2b,#6a7a4a)"></div></div>
  <div class="pillar"><h3>COLOR</h3><p>Colorful &amp; Cheerful Cafe, Street &amp; Park Furniture</p><div class="pic" role="img" aria-label="Blue and yellow metal benches" style="background:linear-gradient(135deg,#4b63a8,#e3b834)"></div></div>
  <div class="pillar"><h3>LIGHT</h3><p>Illuminated Planters &amp; Solar Seating</p><div class="pic" role="img" aria-label="Timber bench with lit planter" style="background:linear-gradient(135deg,#8a5a3a,#d8d0c0)"></div></div>
</section>

<section class="photo parklet darkline">
  <div class="bg" role="img" aria-label="Woman walking past a street parklet with railings"></div>
  <div class="shade"></div>
  <div class="inner">
    <div class="box">
      <h2>CURBLINE PARKLET KITS</h2>
      <ul><li>Adds outdoor seating and dining</li><li>Fits sloping streets and uneven curbs</li><li>Accessible, comfortable, adaptable</li><li>Temporary or permanent</li></ul>
      <span class="btn">MORE INFO</span>
    </div>
  </div>
</section>

<section class="split cafe">
  <div class="copy">
    <h2>BRIGHT, CHEERFUL<br>CAFE FURNITURE</h2>
    <ul><li>Aluminum or Steel</li><li>Fixed mount or loose</li><li>Stackable chairs, benches, tables</li><li>More colors, more fun, more enjoyment</li><li>Durable cafe and street furniture in bright cheerful colors</li></ul>
    <span class="btn">LEARN MORE</span>
  </div>
  <div class="tiles">
    <div class="tile wide"><div role="img" aria-label="White and colored cafe chairs and tables" style="background:linear-gradient(90deg,#e8e8e8,#e0c04a,#d85a3a)"></div></div>
    <div class="tile"><div role="img" aria-label="Blue metal bench" style="background:linear-gradient(135deg,#3f58a0,#c9a235)"></div></div>
    <div class="tile"><div role="img" aria-label="Red cafe table set" style="background:linear-gradient(135deg,#c63a2e,#e1a92e)"></div></div>
  </div>
</section>

<section class="photo porcelain darkline">
  <div class="bg" role="img" aria-label="Porcelain planters beside a pool"></div>
  <div class="shade"></div>
  <div class="inner">
    <h2>PORCELAIN PLANTERS, TABLES,<br>CHAIRS &amp; BENCHES</h2>
    <ul><li>New combination of paving, planters and outdoor furniture</li><li>Strong, durable, fade resistant, low maintenance porcelain</li><li>80+ color options</li></ul>
    <span class="btn">LEARN MORE</span>
  </div>
</section>

<section class="split bench">
  <div class="copy">
    <h2>BENCH SEATING WITH<br>COLOR &amp; STYLE</h2>
    <ul><li>Aluminum or Steel</li><li>Fixed mount or loose</li><li>Stackable chairs, benches, tables</li><li>More colors, more fun, more enjoyment</li><li>Durable cafe and street furniture in bright cheerful colors</li></ul>
    <span class="btn">LEARN MORE</span>
  </div>
  <div class="tiles">
    <div class="tile"><div role="img" aria-label="Timber slat benches" style="background:linear-gradient(135deg,#9a6a3a,#5a4030)"></div></div>
    <div class="tile"><div role="img" aria-label="Timber and concrete bench" style="background:linear-gradient(135deg,#b07a4a,#8a8a8a)"></div></div>
    <div class="tile wide"><div role="img" aria-label="Colorful modular round seats" style="background:linear-gradient(90deg,#7ac5c8,#e6c65a,#e58a6a,#6ab0c8)"></div></div>
  </div>
</section>

<section class="photo illum darkline">
  <div class="bg" role="img" aria-label="Lit patterned metal planters at night"></div>
  <div class="shade"></div>
  <div class="inner">
    <h2>ILLUMINATED PLANTERS</h2>
    <ul><li>PANELS</li><li>Planters with personality. Bright, light and airy</li><li>Powder coated aluminum</li><li>Integrated LED lighting</li></ul>
    <span class="btn">LEARN MORE</span>
  </div>
</section>

<section class="split modular">
  <div class="copy">
    <h2>MODULAR PLANTERS<br>&amp; BENCH SEATING</h2>
    <ul><li>Extendable to any length</li><li>Integrated bench seating</li><li>70+ porcelain color options</li><li>Steel framed planters with porcelain or tile panels</li></ul>
    <span class="btn">LEARN MORE</span>
  </div>
  <div class="tiles">
    <div class="tile"><div role="img" aria-label="Dark square planter with plant" style="background:linear-gradient(180deg,#4a7a3a,#3a3a3a)"></div></div>
    <div class="tile"><div role="img" aria-label="Grey modular planter bench" style="background:linear-gradient(135deg,#8a8a8a,#4a4a4a)"></div></div>
  </div>
</section>

<section class="photo solar darkline">
  <div class="bg" role="img" aria-label="Solar bench in a park"></div>
  <div class="shade"></div>
  <div class="inner">
    <h2>SOLAR BENCH SEATING</h2>
    <ul><li>Custom solar bench</li><li>Integrated solar and device charging</li><li>Tool-free for simple assembly</li><li>Another tool free for simple assembly</li></ul>
    <span class="btn">LEARN MORE</span>
  </div>
</section>

<footer class="footer">
  <div class="about">
    <h4>ABOUT US</h4>
    <p>Velmoreq Civic creates furniture and site products for cities, campuses and commercial spaces. We combine durable materials with bright color and thoughtful design to make streets more welcoming. Our team works with planners, architects and businesses to deliver parklets, seating and planters that suit each place. Visit velmoreq.example to learn more about our range.</p>
  </div>
  <div class="res">
    <h4>RESOURCES</h4>
    <ul><li>SOLAR SPEC SHEETS</li><li>PARKLET RESOURCES</li><li>PARKLETS &amp; PLANTERS</li><li>SOLAR BENCH SEATING</li><li>PORCELAIN PLANTERS</li><li>ILLUMINATED PLANTERS</li></ul>
  </div>
  <div class="quick">
    <h4>QUICK LINKS</h4>
    <ul><li>CURBLINE</li><li>SOLAR</li><li>FURNITURE</li><li>CONTACT</li></ul>
    <div class="social"></div>
  </div>
</footer>
<div class="bottombar">Velmoreq Civic © 2020 — All Rights Reserved</div>
</body>
</html>
```